Velkar Films, LLC needs a business card with a great Toucan Graphic!

Our current business card has a graphic image of a Toucan bird as a play on the word "Velkar" which is a small independent film company located here in California. I have been using this image as a mockup, but it is a copyrighted image, so we need something that is original art which will not put us in jeopardy down the road...

We definitely still want an image of a toucan however (not, as some have suggested, two "cans" of film or some other play on the word).

I have uploaded a pdf file of my OLD business card.

Thanks and look forward to reviewing the designs!

Dane

Target Market(s)

Filmmakers, distribution and production executives, other professionals in the filmmaking world,

Industry/Entity Type

Business

Contact Information for Business Card

Dane Pryseth, Writer/Director
Velkar Films, LLC
517 Harrowgate Lane
Larkhaven, California 92057

Cell: 555.203.8817
Email: dane@velkarfilms.com

Font styles to use
Sans Serif

Requirements
Must have
• A toucan bird as our logo. Velkar Films, LLC (capital T and C in Velkar)
Should not have
• Anything else other than a toucan bird as a play on the word "Velkar"

```html
<!DOCTYPE html>
<html lang="en">
<head>
<meta charset="utf-8">
<title>Velkar Films — Business Card</title>
<link href="https://fonts.googleapis.com/css2?family=Montserrat:wght@400;500;600;700&display=swap" rel="stylesheet">
<style>
  :root {
    --backdrop: #3a3c40;
    --card: #ffffff;
    --ink: #111111;
    --navy: #2a2a78;
    --band: #000000;
    --band-text: #ffffff;
    --rule: #555555;
  }
  html, body {
    margin: 0;
    width: 1200px;
    height: 1000px;
    overflow: hidden;
    background: var(--backdrop);
    font-family: "Montserrat", Arial, sans-serif;
  }
  .card {
    position: absolute;
    left: 100px;
    top: 214px;
    width: 1000px;
    height: 572px;
    background: var(--card);
    border-radius: 36px;
    overflow: hidden;
    box-shadow: 0 14px 40px rgba(0,0,0,0.35);
  }
  .brand {
    position: absolute;
    top: 52px;
    left: 0;
    right: 0;
    display: flex;
    flex-direction: column;
    align-items: center;
  }
  .brand-mark {
    width: 150px;
    height: 150px;
    background: var(--band);
  }
  .brand-name {
    margin-top: 18px;
    font-size: 52px;
    font-weight: 600;
    color: var(--navy);
    letter-spacing: 1px;
    line-height: 1;
  }
  .brand-address {
    margin-top: 12px;
    font-size: 17px;
    font-weight: 500;
    color: var(--ink);
    white-space: nowrap;
  }
  .details {
    position: absolute;
    top: 368px;
    left: 0;
    right: 0;
    display: flex;
    justify-content: center;
    align-items: center;
    gap: 30px;
  }
  .person-name {
    font-size: 27px;
    font-weight: 700;
    color: var(--ink);
    line-height: 1.15;
    white-space: nowrap;
  }
  .person-title {
    font-size: 27px;
    font-weight: 400;
    color: var(--ink);
    line-height: 1.15;
    white-space: nowrap;
  }
  .divider {
    width: 1px;
    height: 70px;
    background: var(--rule);
  }
  .contact {
    list-style: none;
    margin: 0;
    padding: 0;
    font-size: 19px;
    font-weight: 500;
    color: var(--ink);
    white-space: nowrap;
  }
  .contact li {
    display: flex;
    align-items: center;
    gap: 8px;
    margin: 4px 0;
  }
  .contact svg { width: 22px; height: 22px; flex: none; }
  .footer-band {
    position: absolute;
    left: 0;
    right: 0;
    bottom: 0;
    height: 86px;
    background: var(--band);
    border-top: 6px solid var(--navy);
    display: flex;
    align-items: center;
    justify-content: center;
  }
  .website {
    color: var(--band-text);
    font-size: 26px;
    font-weight: 400;
    letter-spacing: 1.5px;
  }
</style>
</head>
<body>
  <div class="card">
    <header class="brand">
      <div class="brand-mark" aria-hidden="true"></div>
      <div class="brand-name">VELKAR FILMS</div>
      <div class="brand-address">517 Harrowgate Lane Larkhaven, California 92057</div>
    </header>

    <section class="details">
      <div class="person">
        <div class="person-name">DANE PRYSETH</div>
        <div class="person-title">WRITER/DIRECTOR</div>
      </div>
      <div class="divider"></div>
      <ul class="contact">
        <li>
          <svg viewBox="0 0 24 24" aria-hidden="true">
            <circle cx="12" cy="12" r="11" fill="var(--navy)"/>
            <path d="M8.5 6.5c.6-.4 1.3-.2 1.6.4l1 1.8c.3.5.1 1.1-.3 1.4l-.7.5c.5 1.2 1.4 2.2 2.6 2.8l.5-.7c.3-.4.9-.6 1.4-.3l1.8 1c.6.3.8 1 .4 1.6-.8 1.2-2 1.6-3.2 1.1-2.7-1.1-4.8-3.2-5.8-5.9-.4-1.2 0-2.4.7-3.2z" fill="#fff"/>
          </svg>
          555.203.8817
        </li>
        <li>
          <svg viewBox="0 0 24 24" aria-hidden="true">
            <circle cx="12" cy="12" r="11" fill="var(--navy)"/>
            <rect x="6.5" y="8" width="11" height="8" rx="1" fill="#fff"/>
            <path d="M6.8 8.4 12 12.4l5.2-4" fill="none" stroke="var(--navy)" stroke-width="1.2"/>
          </svg>
          DANE@VELKARFILMS.COM
        </li>
      </ul>
    </section>

    <footer class="footer-band">
      <span class="website">WWW.VELKARFILMS.COM</span>
    </footer>
  </div>
</body>
</html>
```